Full service residential and commercial painting
Finest quality attention to detail
All workmanship guaranteed
Email :brunomdufay@postvale.fr
Mobile: 0417386250
Industry/Entity Type
Residential
Contact Information for Business Card
Marten Dufay painting & decorating
Requirements
Nice to have
- Am thinking about someone can be painting my name on the card with MD painting with the logos of brush,pot tray and roller sleeves

```html
<!DOCTYPE html>
<html lang="en">
<head>
<meta charset="utf-8">
<title>Marten Dufay painting &amp; decorating — identity and business card</title>
<link rel="stylesheet" href="https://fonts.googleapis.com/css2?family=Carlito:ital,wght@0,400;0,700;1,400&display=swap">
<style>
  :root {
    --stage: #a9a9a9;
    --card: #050505;
    --purple: #a53bb0;
    --blue: #1f86d2;
    --grey: #8a8a8a;
    --grey-dark: #555555;
    --silhouette: #6b6b6b;
  }
  html, body {
    margin: 0;
    padding: 0;
    width: 1200px;
    height: 900px;
    overflow: hidden;
    background: var(--stage);
    font-family: "Carlito", "Calibri", sans-serif;
  }
  .canvas {
    position: relative;
    width: 1200px;
    height: 900px;
  }

  /* Brand lockup on the stage */
  .brand-lockup {
    position: absolute;
    left: 80px;
    top: 86px;
    display: flex;
    align-items: center;
    gap: 22px;
  }
  .brand-dot {
    width: 58px;
    height: 58px;
    border-radius: 50%;
    background: var(--purple);
    flex: none;
  }
  .brand-name {
    color: var(--grey-dark);
    font-weight: 400;
    line-height: 1;
  }
  .brand-name .name-line {
    display: block;
    font-size: 62px;
  }
  .brand-name .trade-line {
    display: block;
    font-size: 38px;
    margin-top: 4px;
  }

  /* Business card, flat */
  .business-card {
    position: absolute;
    left: 440px;
    top: 440px;
    width: 660px;
    height: 370px;
    background: var(--card);
    border-radius: 16px;
    overflow: hidden;
  }
  .card-brand {
    position: absolute;
    left: 44px;
    top: 40px;
    display: flex;
    align-items: center;
    gap: 14px;
  }
  .card-brand .brand-dot {
    width: 34px;
    height: 34px;
  }
  .card-brand .brand-name {
    color: var(--grey);
  }
  .card-brand .name-line { font-size: 40px; }
  .card-brand .trade-line { font-size: 24px; margin-top: 2px; }

  .contact {
    position: absolute;
    right: 250px;
    top: 150px;
    text-align: right;
  }
  .contact-name {
    margin: 0 0 12px;
    font-size: 22px;
    font-weight: 700;
    letter-spacing: 0.5px;
  }
  .contact-name .first { color: var(--purple); }
  .contact-name .last { color: var(--blue); }
  .contact-line {
    margin: 0 0 6px;
    font-size: 15px;
    color: var(--grey);
  }

  .services {
    position: absolute;
    left: 70px;
    bottom: 60px;
    margin: 0;
    padding: 0;
    list-style: none;
    color: var(--purple);
    font-style: italic;
    font-size: 15px;
    line-height: 1.3;
  }

  .painter-figure {
    position: absolute;
    right: 60px;
    bottom: 40px;
    width: 130px;
    height: 210px;
    background: linear-gradient(180deg, #7a7a7a, var(--silhouette));
    border-radius: 40px 40px 8px 8px;
  }
</style>
</head>
<body>
<main class="canvas">

  <header class="brand-lockup">
    <span class="brand-dot" aria-hidden="true"></span>
    <div class="brand-name">
      <span class="name-line">Marten Dufay</span>
      <span class="trade-line">painting &amp; decorating</span>
    </div>
  </header>

  <section class="business-card" aria-label="Business card">
    <div class="card-brand">
      <span class="brand-dot" aria-hidden="true"></span>
      <div class="brand-name">
        <span class="name-line">Marten Dufay</span>
        <span class="trade-line">painting &amp; decorating</span>
      </div>
    </div>

    <div class="contact">
      <p class="contact-name"><span class="first">BRUNO</span> <span class="last">DUFAY</span></p>
      <p class="contact-line">0417 386 250</p>
      <p class="contact-line">brunomdufay@postvale.fr</p>
    </div>

    <ul class="services">
      <li>Full service residential and commercial painting</li>
      <li>Finest quality attention to detail</li>
      <li>All workmanship guaranteed</li>
    </ul>

    <div class="painter-figure" role="img" aria-label="Grey silhouette of a painter holding a paint roller up against the wall"></div>
  </section>

</main>
</body>
</html>
```